Business card for Harbor Crafters
Looking for creativity
Professional
Dominic Farrow
Owner Operator
47 S Pell Avenue
Middletown, DE 19842
@domfarrow
craftharborco@mailvane.com
www.craftharborco.com
Looking for a creative business card for my company. I have a logo and like the feel of it. The business card should have a contemporary feel and be interesting.
The name of the company and the website

```html
<!DOCTYPE html>
<html lang="en">
<head>
<meta charset="utf-8">
<title>Harbor Crafters Stationery</title>
<link href="https://fonts.googleapis.com/css2?family=Lato:wght@400;700&display=swap" rel="stylesheet">
<style>
:root{
  --bg:#ece7df;
  --paper:#ffffff;
  --brand:#2f5fa8;
  --brand-dark:#264d8a;
  --slate:#7d8087;
  --ink:#4a4d52;
  --faint:#eef1f6;
  --label:#6f6a63;
}
*{box-sizing:border-box;margin:0;padding:0}
html,body{width:1200px;height:274px;overflow:hidden;background:var(--bg);font-family:"Lato",sans-serif;color:var(--ink)}
.stage{position:relative;width:1200px;height:274px}
.section-title{position:absolute;font-size:9px;color:var(--label);letter-spacing:.3px}
.piece{position:absolute;box-shadow:0 1px 3px rgba(0,0,0,.18)}
.card{border-radius:3px;padding:7px 8px;overflow:hidden}
.card--white{background:var(--paper)}
.card--blue{background:var(--brand);display:flex;align-items:center;justify-content:center}
.card--gray{background:var(--slate);display:flex;align-items:center;justify-content:center}
.brand{display:flex;align-items:center;gap:3px;font-weight:700;color:var(--brand);letter-spacing:1px;white-space:nowrap}
.brand i{display:inline-block;background:var(--brand)}
.card--blue .brand,.card--gray .brand{color:var(--paper)}
.card--blue .brand i,.card--gray .brand i{background:var(--paper)}
.card .brand{font-size:9px}
.card .brand i{width:6px;height:6px}
.contact{margin-top:5px;font-size:4.5px;line-height:6px;color:var(--ink)}
.contact b{display:block;font-size:5.5px;color:var(--brand-dark)}
.piece-label{position:absolute;font-size:6px;color:var(--label);text-align:center}
.letterhead{background:var(--paper);padding:8px 10px}
.letterhead .brand{font-size:8px}
.letterhead .brand i{width:5px;height:5px}
.letterhead .meta{position:absolute;top:10px;right:10px;font-size:4px;line-height:5px;text-align:right;color:var(--ink)}
.letterhead .watermark{position:absolute;left:0;right:0;top:44%;text-align:center;font-weight:700;font-size:26px;letter-spacing:3px;color:var(--faint)}
.letterhead .footer{position:absolute;left:0;right:0;bottom:8px;text-align:center;font-size:4px;color:var(--ink)}
.option-label{position:absolute;top:232px;font-size:11px;color:var(--label)}
.envelope{background:var(--paper);overflow:hidden}
.envelope--blue{background:var(--brand)}
.envelope--gray{background:var(--slate)}
.envelope svg{display:block}
.envelope-card{background:var(--paper);padding:3px 4px}
.envelope-card .brand{font-size:5px;letter-spacing:.5px}
.envelope-card .brand i{width:4px;height:4px}
</style>
</head>
<body>
<main class="stage">
  <p class="section-title" style="left:24px;top:14px">Stationery Concept</p>

  <!-- business cards -->
  <div class="piece card card--white" style="left:29px;top:36px;width:115px;height:54px">
    <div class="brand"><i></i>HARBOR</div>
    <p class="contact"><b>Dominic Farrow</b>Owner Operator<br>craftharborco@mailvane.com</p>
  </div>
  <p class="piece-label" style="left:29px;top:94px;width:115px">White Front</p>

  <div class="piece card card--white" style="left:158px;top:36px;width:135px;height:54px">
    <div class="brand"><i></i>HARBOR CRAFTERS</div>
    <p class="contact">47 S Pell Avenue, Middletown, DE 19842<br>@domfarrow<br>www.craftharborco.com</p>
  </div>
  <p class="piece-label" style="left:158px;top:94px;width:135px">White Back</p>

  <div class="piece card card--blue" style="left:34px;top:120px;width:110px;height:46px">
    <div class="brand"><i></i>HARBOR</div>
  </div>
  <p class="piece-label" style="left:34px;top:170px;width:110px">Blue Back</p>

  <div class="piece card card--gray" style="left:158px;top:120px;width:130px;height:46px">
    <div class="brand"><i></i>HARBOR</div>
  </div>
  <p class="piece-label" style="left:158px;top:170px;width:130px">Gray Back</p>

  <!-- letterheads -->
  <div class="piece letterhead" style="left:302px;top:20px;width:168px;height:204px">
    <div class="brand"><i></i>HARBOR</div>
    <p class="meta">47 S Pell Avenue<br>Middletown, DE 19842</p>
    <p class="watermark">HARBOR</p>
  </div>
  <p class="option-label" style="left:360px">Option 1</p>

  <div class="piece letterhead" style="left:482px;top:20px;width:147px;height:204px">
    <div class="brand"><i></i>HARBOR</div>
    <p class="meta">www.craftharborco.com<br>@domfarrow</p>
    <p class="watermark" style="font-size:22px">HARBOR</p>
  </div>
  <p class="option-label" style="left:533px">Option 2</p>

  <div class="piece letterhead" style="left:638px;top:20px;width:144px;height:204px">
    <div class="brand" style="justify-content:center"><i></i>HARBOR</div>
    <p class="watermark" style="font-size:22px">HARBOR</p>
    <p class="footer">47 S Pell Avenue · craftharborco@mailvane.com</p>
  </div>
  <p class="option-label" style="left:688px">Option 3</p>

  <div class="piece letterhead" style="left:804px;top:20px;width:156px;height:204px">
    <div class="brand" style="justify-content:center"><i></i>HARBOR</div>
    <p class="watermark" style="font-size:24px">HARBOR</p>
    <p class="footer">www.craftharborco.com</p>
  </div>
  <p class="option-label" style="left:858px">Option 3</p>

  <!-- envelopes -->
  <p class="section-title" style="left:1090px;top:30px;font-size:7px">Envelope Design</p>

  <div class="piece envelope envelope--blue" style="left:1032px;top:44px;width:70px;height:26px">
    <svg width="70" height="26" viewBox="0 0 70 26"><path d="M0 0 L35 14 L70 0" fill="none" stroke="#ffffff" stroke-opacity=".5" stroke-width="1"/></svg>
  </div>
  <div class="piece envelope" style="left:1032px;top:80px;width:70px;height:26px">
    <svg width="70" height="26" viewBox="0 0 70 26"><path d="M0 0 L35 14 L70 0" fill="none" stroke="#2f5fa8" stroke-width="1.5"/></svg>
  </div>
  <div class="piece envelope envelope--gray" style="left:1032px;top:116px;width:70px;height:26px">
    <svg width="70" height="26" viewBox="0 0 70 26"><path d="M0 0 L35 14 L70 0" fill="none" stroke="#ffffff" stroke-opacity=".5" stroke-width="1"/></svg>
  </div>
  <div class="piece envelope" style="left:1032px;top:152px;width:70px;height:26px">
    <svg width="70" height="26" viewBox="0 0 70 26"><path d="M0 0 L35 14 L70 0" fill="none" stroke="#7d8087" stroke-width="1.5"/></svg>
  </div>

  <div class="piece envelope-card" style="left:1110px;top:56px;width:78px;height:24px"><div class="brand"><i></i>HARBOR</div></div>
  <div class="piece envelope-card" style="left:1110px;top:92px;width:78px;height:24px"><div class="brand"><i></i>HARBOR</div></div>
  <div class="piece envelope-card" style="left:1110px;top:128px;width:78px;height:24px"><div class="brand"><i></i>HARBOR</div></div>
  <div class="piece envelope-card" style="left:1110px;top:164px;width:78px;height:24px"><div class="brand"><i></i>HARBOR</div></div>
</main>
</body>
</html>
```